1/2 Page add for MERLT Conference

We are looking for a 1/2 page ad to support the annual MERLT conference. I want to encourage the attendees to come to our both so we can explain how they can save money on food and supplies. here is a link to the conference. https://www.merlt-example.org/conference/ here is our website www.pantryhubdirect-example.com - the what we do can be captured in the ad. We will be at booth 505. Our goal is to get people to our booth #505 to explain the services that we provide –

Discounted food pricing
Free menu planning/design
Use of Registered Dietitian
Huge selection of discounted PPE and other necessary supplies to run any child care center

We have over 6000 members in 46 States and work with both small and large food distributors. We have been a sponsor of the association for the last 10 years.

Target Market(s)

Child care centers

Requirements
Must have
• Booth number -outline of what we do --- Stress we are a FREE service getting our members reduced pricing on food and supplies

```html
<!DOCTYPE html>
<html lang="en">
<head>
<meta charset="utf-8">
<title>MERLT Conference Half-Page Ad — PantryHub Direct</title>
<link rel="stylesheet" href="https://fonts.googleapis.com/css2?family=Figtree:wght@400;500;600;700;800&display=swap">
<style>
  :root {
    --page-bg: #3a3a3a;
    --card-bg: #ffffff;
    --brand-blue: #2f86e0;
    --brand-green: #3aa335;
    --ink: #111111;
    --ink-soft: #1c1c1c;
    --muted: #7a7a7a;
    --on-photo: #ffffff;
  }
  * { box-sizing: border-box; margin: 0; padding: 0; }
  html, body { width: 1200px; height: 1200px; overflow: hidden; }
  body {
    background: var(--page-bg);
    font-family: "Figtree", Arial, sans-serif;
    position: relative;
  }
  .ad {
    position: absolute;
    left: 30px; top: 213px;
    width: 1140px; height: 773px;
    background: var(--card-bg);
    overflow: hidden;
  }
  .ad-content { position: absolute; left: 0; top: 0; width: 769px; height: 100%; }
  .headline {
    position: absolute; left: 32px; top: 30px;
    font-weight: 700; font-size: 84px; line-height: 65px;
    letter-spacing: -1.5px; color: var(--brand-green);
  }
  .headline span { display: block; white-space: nowrap; }
  .headline .year { color: var(--brand-blue); }
  .rule {
    position: absolute; left: 33px; top: 319px;
    width: 592px; height: 2px; background: var(--ink);
  }
  .event-info {
    position: absolute; left: 32px; top: 333px;
    font-weight: 700; font-size: 31px; color: var(--ink);
    white-space: nowrap; letter-spacing: -0.4px;
  }
  .services {
    position: absolute; left: 32px; top: 456px;
    list-style: none; font-weight: 400; font-size: 24px;
    line-height: 25px; color: var(--ink-soft); width: 620px;
  }
  .services li { position: relative; padding-left: 22px; margin-bottom: 12px; }
  .services li::before {
    content: ""; position: absolute; left: 0; top: 6px;
    width: 11px; height: 11px; background: var(--brand-green);
  }
  .services .pair { display: flex; gap: 10px; padding-left: 0; white-space: nowrap; }
  .services .pair::before { display: none; }
  .services .pair span { position: relative; padding-left: 22px; }
  .services .pair span::before {
    content: ""; position: absolute; left: 0; top: 6px;
    width: 11px; height: 11px; background: var(--brand-green);
  }
  .brand {
    position: absolute; left: 55px; top: 650px;
    display: flex; align-items: center; gap: 12px;
  }
  .brand-mark { width: 32px; height: 32px; background: var(--brand-green); }
  .brand-name { font-weight: 500; font-size: 36px; color: var(--muted); letter-spacing: -0.8px; white-space: nowrap; }
  .contact {
    position: absolute; left: 32px; top: 727px;
    display: flex; align-items: center; gap: 12px;
    font-size: 16px; color: var(--ink-soft);
    white-space: nowrap; letter-spacing: -0.2px;
  }
  .contact-item { display: flex; align-items: center; gap: 4px; }
  .contact svg { width: 13px; height: 13px; flex: none; }
  .divider {
    position: absolute; left: 509px; top: 641px;
    width: 3px; height: 111px; background: var(--brand-blue);
  }
  .booth-callout { position: absolute; left: 534px; top: 682px; white-space: nowrap; }
  .booth-callout .lead { font-weight: 800; font-size: 26px; line-height: 28px; color: var(--ink); }
  .booth-callout .booth { font-weight: 700; font-size: 38px; line-height: 40px; color: var(--brand-blue); letter-spacing: -0.5px; }
  .city-photo {
    position: absolute; right: 0; top: 0;
    width: 371px; height: 100%;
    background:
      linear-gradient(180deg, rgba(0,0,0,0) 70%, rgba(40,30,10,0.65) 100%),
      linear-gradient(180deg, #7dc3ef 0%, #9aa7dd 25%, #8a6ea8 45%, #b0578a 62%, #d8663c 78%, #6a4a2a 100%);
  }
  .member-note {
    position: absolute; right: 0; top: 679px; width: 371px;
    padding-left: 32px;
    font-weight: 500; font-size: 21px; line-height: 21px;
    color: var(--on-photo); text-transform: uppercase; letter-spacing: -0.2px;
    white-space: nowrap;
  }
  .member-note strong { font-weight: 800; color: var(--brand-blue); }
</style>
</head>
<body>
  <article class="ad">
    <div class="ad-content">
      <h1 class="headline">
        <span class="year">2022</span>
        <span>National Child</span>
        <span>Nutrition</span>
        <span>Conference</span>
      </h1>
      <div class="rule"></div>
      <p class="event-info">April 18-22, 2022 | New Orleans, Louisiana</p>

      <ul class="services">
        <li class="pair"><span>Discounted Food Pricing</span><span>Free Menu Planning/Design</span></li>
        <li>Use of Registered Dietitian</li>
        <li>Huge selection of discounted PPE and other necessary supplies to run any child care center</li>
      </ul>

      <div class="brand">
        <div class="brand-mark"></div>
        <div class="brand-name">PantryHub Direct</div>
      </div>

      <div class="contact">
        <span class="contact-item">
          <svg viewBox="0 0 24 24" aria-hidden="true"><path fill="#2f86e0" d="M6.6 10.8a15.1 15.1 0 0 0 6.6 6.6l2.2-2.2a1 1 0 0 1 1-.25 11.4 11.4 0 0 0 3.6.57 1 1 0 0 1 1 1V20a1 1 0 0 1-1 1A17 17 0 0 1 3 4a1 1 0 0 1 1-1h3.5a1 1 0 0 1 1 1c0 1.25.2 2.45.57 3.57a1 1 0 0 1-.25 1z"/></svg>
          800-555-0147
        </span>
        <span class="contact-item">
          <svg viewBox="0 0 24 24" aria-hidden="true" fill="none" stroke="#2f86e0" stroke-width="2"><circle cx="12" cy="12" r="9"/><path d="M3 12h18M12 3c3 3 3 15 0 18M12 3c-3 3-3 15 0 18"/></svg>
          www.pantryhubdirect-example.com
        </span>
      </div>

      <div class="divider"></div>
      <div class="booth-callout">
        <p class="lead">MEET US AT</p>
        <p class="booth">BOOTH #505</p>
      </div>
    </div>

    <div class="city-photo" role="img" aria-label="Photo of a New Orleans French Quarter street at dusk with balconies, flags and glowing lights"></div>
    <p class="member-note">Members gets <strong>Free Services</strong><br>on reduced pricing on<br>food &amp; supplies</p>
  </article>
</body>
</html>
```